Modern, pro female massage business needs business card design

We are a boutique, pro women's sports and remedial massage studio based in Singapore - we have a logo already (see attached image) and need to design a business card that reflects an elegant, modern and feminine feel using this logo.

We are focussed on a very local market and need to give a professional yet warm feeling.

Details for the card include (layout of your choice):

Talvina Brisk
Call, SMS or ChatBeam: 8317 6092
Email: tealmarrow@quenfold.com
Address: The Harbourview at Dunmore
82 Dunmore Road, East Coast, Singapore

To incorporate the OVAR logo (www.ovarglobe.co.uk) would be appreciated - see attached file.

Industry/Entity Type

Massage

Requirements
Nice to have
• We like the idea of using an embossed style card. Solid colour on the reverse - embossed on the front; four colour printing is okay.
Should not have
• It should not be uber 'girly girl' if that makes any sense. The logo is already colourful

```html
<!DOCTYPE html>
<html lang="en">
<head>
<meta charset="utf-8">
<title>Talvina Brisk – Business Card</title>
<link rel="stylesheet" href="https://fonts.googleapis.com/css2?family=Fira+Sans:wght@400;500&family=Russo+One&display=swap">
<style>
  :root {
    --backdrop: #2b2b2b;
    --card-white: #ffffff;
    --card-texture: #f1f1f1;
    --brand-pink: #ec1e8c;
    --name-green: #a3cc3a;
    --name-green-deep: #7fa52a;
    --tagline-grey: #5a5a5a;
    --contact-white: #ffffff;
  }
  * { box-sizing: border-box; margin: 0; padding: 0; }
  html, body {
    width: 1200px;
    height: 673px;
    overflow: hidden;
    background: var(--backdrop);
  }
  .stage {
    position: relative;
    width: 1200px;
    height: 673px;
  }
  .business-card {
    position: absolute;
    left: 150px;
    top: 45px;
    width: 900px;
    height: 584px;
    background:
      radial-gradient(ellipse at 30% 30%, var(--card-white) 0%, var(--card-texture) 100%);
    display: flex;
    flex-direction: column;
    overflow: hidden;
  }
  .card-face {
    flex: 1;
    display: flex;
    flex-direction: column;
    align-items: center;
    padding-top: 140px;
  }
  .brand-lockup {
    display: flex;
    flex-direction: column;
    align-items: flex-start;
    margin-left: -150px;
  }
  .brand-name {
    display: flex;
    align-items: center;
    gap: 10px;
    font-family: "Fira Sans", sans-serif;
    font-weight: 500;
    font-size: 60px;
    line-height: 1;
    color: var(--brand-pink);
    letter-spacing: -1px;
  }
  .brand-dot {
    width: 22px;
    height: 22px;
    border-radius: 50%;
    background: var(--brand-pink);
  }
  .brand-tagline {
    font-family: "Fira Sans", sans-serif;
    font-size: 20px;
    color: var(--tagline-grey);
    margin-top: 4px;
    margin-left: 34px;
  }
  .holder-name {
    font-family: "Russo One", sans-serif;
    font-size: 82px;
    line-height: 1;
    color: var(--name-green);
    text-transform: uppercase;
    letter-spacing: 2px;
    margin-top: 26px;
    text-shadow: 0 2px 0 var(--name-green-deep);
  }
  .contact-band {
    height: 164px;
    background: var(--brand-pink);
    color: var(--contact-white);
    font-family: "Fira Sans", sans-serif;
    text-align: center;
    padding-top: 28px;
  }
  .contact-address {
    font-size: 27px;
    line-height: 1.3;
  }
  .contact-lines {
    font-size: 17px;
    line-height: 1.35;
    margin-top: 8px;
  }
</style>
</head>
<body>
<main class="stage">
  <article class="business-card">
    <section class="card-face">
      <div class="brand-lockup">
        <div class="brand-name"><span class="brand-dot"></span>tealmarrow</div>
        <div class="brand-tagline">Remedial and sports massage</div>
      </div>
      <h1 class="holder-name">Talvina Brisk</h1>
    </section>
    <footer class="contact-band">
      <p class="contact-address">Address: The Harbourview at Dunmore<br>82 Dunmore Road, East Coast, Singapore</p>
      <p class="contact-lines">Call, SMS or ChatBeam: 8317 6092<br>Email: tealmarrow@quenfold.com</p>
    </footer>
  </article>
</main>
</body>
</html>
```